Need DL Flyer for Real Estate Drops

We need a real estate flyer ,double sided. With content on 1 side like: Want to know what's your house is worth " contact us today and on other side agent details. We are looking for an ongoing partnership with designer so this assignment will be ongoing

```html
<!DOCTYPE html>
<html lang="en">
<head>
<meta charset="utf-8">
<title>Dunewell Real Estate – DL Flyer</title>
<link href="https://fonts.googleapis.com/css2?family=Oswald:wght@500;700&family=Montserrat:wght@400;500;600;700&display=swap" rel="stylesheet">
<style>
  :root{
    --navy:#141b3d;
    --red:#d0202e;
    --white:#ffffff;
    --stage:#dcdcdc;
    --ink-soft:#e9ebf2;
  }
  *{box-sizing:border-box;margin:0;padding:0}
  html,body{width:734px;height:1200px;overflow:hidden}
  body{background:var(--stage);font-family:"Montserrat",sans-serif;position:relative}
  .flyer{position:absolute;top:250px;width:330px;height:700px;overflow:hidden;box-shadow:0 10px 24px rgba(0,0,0,.28)}
  .flyer--front{left:22px;background:var(--white)}
  .flyer--back{left:382px;background:var(--navy)}

  .brand{position:absolute;display:flex;align-items:center;gap:14px}
  .brand__mark{width:52px;height:52px;border-radius:6px;flex:none}
  .brand__name{font-family:"Montserrat",sans-serif;font-weight:600;font-size:25px;line-height:1.05}
  .flyer--front .brand{left:34px;top:32px}
  .flyer--front .brand__mark{background:var(--red)}
  .flyer--front .brand__name{color:var(--navy)}
  .flyer--back .brand{left:38px;top:30px}
  .flyer--back .brand__mark{background:var(--navy)}
  .flyer--back .brand__name{color:var(--white)}

  .house-photo{position:absolute;left:0;top:135px;width:330px;height:235px;
    background:linear-gradient(180deg,#f6f7f9 0%,#d3d6db 35%,#b7aa98 70%,#6f5a44 100%)}
  .chevron{position:absolute;left:0;top:300px;width:330px;height:100px;display:block}
  .front-panel{position:absolute;left:0;top:398px;width:330px;height:302px;background:var(--navy)}

  .headline{position:absolute;left:0;top:388px;width:330px;text-align:center;font-family:"Oswald",sans-serif;text-transform:uppercase;letter-spacing:-.5px}
  .headline__lead{display:block;color:var(--white);font-weight:500;font-size:45px;line-height:48px}
  .headline__accent{display:block;color:var(--red);font-weight:700;font-size:47px;line-height:50px}

  .cta{position:absolute;left:28px;width:274px;height:24px}
  .cta::before{content:"";position:absolute;left:0;right:0;top:50%;height:2px;background:var(--red)}
  .cta__pill{position:relative;display:block;margin:0 auto;width:fit-content;padding:0 12px;height:24px;line-height:24px;border-radius:12px;background:var(--red);color:var(--white);font-weight:700;font-size:13px}
  .flyer--front .cta{top:613px}
  .flyer--back .cta{top:533px}

  .hotline{position:absolute;left:0;top:645px;width:330px;display:flex;justify-content:center;align-items:center;gap:8px;color:var(--white);font-weight:700;font-size:28px}
  .hotline__icon{width:26px;height:26px;border-radius:4px;background:var(--red);display:flex;align-items:center;justify-content:center}

  .back-top{position:absolute;left:0;top:0;width:330px;height:253px;background:var(--red)}
  .agent-ring{position:absolute;left:57px;top:140px;width:218px;height:218px;border-radius:50%;background:var(--red)}
  .agent-photo{position:absolute;left:64px;top:147px;width:204px;height:204px;border-radius:50%;
    background:linear-gradient(180deg,#f2f2f2 0%,#cfcfcf 55%,#8d8d8d 100%)}
  .agent-name{position:absolute;left:0;top:376px;width:330px;text-align:center;color:var(--red);font-weight:700;font-size:28px;text-transform:uppercase;letter-spacing:-.3px}
  .agent-role{position:absolute;left:0;top:416px;width:330px;text-align:center;color:var(--white);font-size:17px;line-height:24px}
  .social{position:absolute;left:0;top:486px;width:330px;display:flex;justify-content:center;gap:10px}
  .social__dot{width:28px;height:28px;border-radius:50%;background:var(--red)}
  .contact-icons{position:absolute;left:0;top:570px;width:330px;display:flex;justify-content:center;gap:15px}
  .contact-icons span{width:24px;height:24px;border-radius:50%;background:var(--red);display:flex;align-items:center;justify-content:center}
  .contact-list{position:absolute;left:0;top:602px;width:330px;text-align:center;color:var(--white);font-weight:600;font-size:12.5px;line-height:18.5px;list-style:none}
  .contact-list .accent{color:var(--red)}
</style>
</head>
<body>

<section class="flyer flyer--front" aria-label="Flyer front">
  <div class="brand">
    <span class="brand__mark"></span>
    <span class="brand__name">Dunewell<br>Real Estate</span>
  </div>
  <div class="house-photo" role="img" aria-label="Photo of a modern single-storey home at dusk with lit windows and a landscaped garden"></div>
  <svg class="chevron" viewBox="0 0 330 100" aria-hidden="true">
    <polygon points="0,27 165,57 330,27 330,100 0,100" fill="var(--red)"/>
    <polygon points="0,42 165,72 330,42 330,100 0,100" fill="var(--navy)"/>
  </svg>
  <div class="front-panel"></div>
  <h1 class="headline">
    <span class="headline__lead">Want to</span>
    <span class="headline__lead">know what's</span>
    <span class="headline__accent">your house</span>
    <span class="headline__accent">is worth</span>
  </h1>
  <div class="cta"><span class="cta__pill">CONTACT US TODAY</span></div>
  <div class="hotline">
    <span class="hotline__icon">
      <svg width="16" height="16" viewBox="0 0 24 24" aria-hidden="true"><path fill="#fff" d="M6.6 10.8a15.1 15.1 0 0 0 6.6 6.6l2.2-2.2a1 1 0 0 1 1-.25 11.4 11.4 0 0 0 3.6.57 1 1 0 0 1 1 1V20a1 1 0 0 1-1 1A17 17 0 0 1 3 4a1 1 0 0 1 1-1h3.5a1 1 0 0 1 1 1c0 1.25.2 2.45.57 3.57a1 1 0 0 1-.25 1z"/></svg>
    </span>
    <span>(03) 9000 1234</span>
  </div>
</section>

<section class="flyer flyer--back" aria-label="Flyer back, agent details">
  <div class="back-top"></div>
  <div class="brand">
    <span class="brand__mark"></span>
    <span class="brand__name">Dunewell<br>Real Estate</span>
  </div>
  <div class="agent-ring"></div>
  <div class="agent-photo" role="img" aria-label="Black and white portrait of the agent in a light suit"></div>
  <h2 class="agent-name">Arjun Kalra</h2>
  <p class="agent-role">Managing Director / LEA,<br>Dunewell Real Estate</p>
  <div class="social" aria-label="Social links">
    <span class="social__dot"></span>
    <span class="social__dot"></span>
  </div>
  <div class="cta"><span class="cta__pill">CONTACT US TODAY</span></div>
  <div class="contact-icons" aria-hidden="true">
    <span><svg width="12" height="12" viewBox="0 0 24 24"><path fill="#fff" d="M12 2a7 7 0 0 0-7 7c0 5.2 7 13 7 13s7-7.8 7-13a7 7 0 0 0-7-7zm0 9.5A2.5 2.5 0 1 1 12 6.5a2.5 2.5 0 0 1 0 5z"/></svg></span>
    <span><svg width="12" height="12" viewBox="0 0 24 24"><path fill="#fff" d="M6.6 10.8a15.1 15.1 0 0 0 6.6 6.6l2.2-2.2a1 1 0 0 1 1-.25 11.4 11.4 0 0 0 3.6.57 1 1 0 0 1 1 1V20a1 1 0 0 1-1 1A17 17 0 0 1 3 4a1 1 0 0 1 1-1h3.5a1 1 0 0 1 1 1c0 1.25.2 2.45.57 3.57a1 1 0 0 1-.25 1z"/></svg></span>
    <span><svg width="12" height="12" viewBox="0 0 24 24"><path fill="#fff" d="M3 5h18v14H3zm2 2v.4l7 4.6 7-4.6V7z"/></svg></span>
    <span><svg width="12" height="12" viewBox="0 0 24 24" fill="none" stroke="#fff" stroke-width="2"><circle cx="12" cy="12" r="9"/><path d="M3 12h18M12 3c3 3.5 3 14.5 0 18M12 3c-3 3.5-3 14.5 0 18"/></svg></span>
  </div>
  <ul class="contact-list">
    <li>14/8 Meridian Way, Larkvale, VIC 3099</li>
    <li>(03) 9000 1234, 0400123456</li>
    <li>arjun@dunewellrealestate.com.au</li>
    <li>www.<span class="accent">dunewellrealestate</span>.com.au</li>
  </ul>
</section>

</body>
</html>
```